2026 Company Line Card

We would like to redesign our current company line card. We send this printed flyer to prospective customers to introduce our company, the brands we represent, and our competitive advantages. Our website is www.valvorimsupply.com, and our phone number is (800) 312-4470. We're a specialty supplier for plumbing material, specifically water and life safety products. Our customers are mostly male, blue-collar contractors, ages 40-60. I have included a pdf of our current flyer and our high-resolution transparent logo. We would also like to highlight certain key points, which include:
Genuine OEM Parts
Technical Assistance from Repair Experts
Repair Information
1-2 day Delivery for the United States
Friendly & Knowledgeable Customer Service
The Largest Parts Inventory In The Nation
Testing Equipment
Full Service Gauge Calibration and Repair

```html
<!DOCTYPE html>
<html lang="en">
<head>
<meta charset="utf-8">
<title>Valvorim Supply Co. – Line Card</title>
<link href="https://fonts.googleapis.com/css2?family=Montserrat:wght@500;600;700;800;900&display=swap" rel="stylesheet">
<style>
  :root{
    --navy:#262b55;
    --navy-deep:#1b1f40;
    --blue:#2350a6;
    --blue-dark:#243a8c;
    --sky:#7fc6f2;
    --sky-light:#b9e3fb;
    --red:#d8243f;
    --white:#ffffff;
    --paper:#f4f4f6;
    --stage:#e6e6ea;
    --ink:#3a3d52;
  }
  *{box-sizing:border-box;margin:0;padding:0}
  html,body{width:1200px;height:900px;overflow:hidden;background:var(--stage);font-family:"Montserrat",sans-serif}
  .line-card{position:absolute;left:300px;top:26px;width:600px;height:848px;background:var(--paper);overflow:hidden;box-shadow:0 6px 24px rgba(0,0,0,.12)}
  .line-card__shapes{position:absolute;inset:0}
  .brand-mark{position:absolute;left:18px;top:78px;width:180px;display:flex;align-items:center;gap:7px;white-space:nowrap}
  .brand-mark__dot{width:11px;height:11px;border-radius:50%;background:var(--red);flex:none}
  .brand-mark__name{font-weight:700;font-size:14px;color:var(--blue);line-height:1.1}
  .hero-text{position:absolute;left:52px;top:176px;width:300px}
  .hero-text__pill{display:inline-block;background:var(--red);color:var(--white);font-weight:800;font-size:11px;letter-spacing:-.2px;padding:4px 14px;border-radius:12px}
  .hero-text__line{color:var(--white);font-weight:900;line-height:1;letter-spacing:-.5px}
  .hero-text__oem{font-size:23px;margin-top:10px}
  .hero-text__repair{font-size:64px;color:var(--sky);margin-top:2px;background:linear-gradient(180deg,var(--sky-light),var(--sky));-webkit-background-clip:text;background-clip:text;-webkit-text-fill-color:transparent}
  .hero-text__info{font-size:35px;color:var(--sky);margin-top:-2px}
  .hero-text__tech{font-size:21px;margin-top:4px}
  .repair-matrix{position:absolute;left:88px;top:500px;width:270px}
  .repair-matrix__title{font-weight:900;font-size:50px;color:var(--blue-dark);line-height:.95;letter-spacing:-1px}
  .repair-matrix__sub{font-weight:900;font-size:37px;color:var(--red);line-height:1;letter-spacing:-.5px}
  .repair-matrix__hint{font-size:7px;font-weight:500;color:var(--ink);margin-top:9px}
  .brand-grid{display:grid;grid-template-columns:repeat(4,58px);gap:9px;margin-top:16px}
  .brand-grid__tile{height:42px;background:var(--white);border-radius:5px;box-shadow:0 1px 4px rgba(0,0,0,.15);display:flex;align-items:center;justify-content:center;font-weight:700;font-size:8.5px;letter-spacing:.2px;color:var(--navy)}
  .advantages{position:absolute;left:396px;top:500px;width:200px;list-style:none}
  .advantages__item{display:flex;align-items:center;gap:10px;height:40px;color:var(--white);font-weight:800;font-size:8.6px;line-height:1.2;text-transform:uppercase}
  .advantages__icon{width:26px;height:26px;flex:none;border-radius:50%;background:var(--white);box-shadow:0 0 0 3px rgba(255,255,255,.35);display:flex;align-items:center;justify-content:center}
  .contact{position:absolute;left:36px;top:768px;color:var(--white)}
  .contact__row{display:flex;align-items:center;gap:9px;margin-bottom:10px}
  .contact__icon{width:26px;height:26px;border-radius:50%;background:var(--blue);box-shadow:0 0 0 3px var(--white);display:flex;align-items:center;justify-content:center;flex:none}
  .contact__label{font-weight:800;font-size:9px;display:block}
  .contact__value{font-weight:500;font-size:10px;display:block}
</style>
</head>
<body>
<main class="line-card">
  <svg class="line-card__shapes" viewBox="0 0 600 848" width="600" height="848">
    <defs>
      <linearGradient id="heroTone" x1="0" y1="0" x2="1" y2="0.3">
        <stop offset="0" stop-color="#1f2447"/>
        <stop offset="0.45" stop-color="#2f3462"/>
        <stop offset="0.72" stop-color="#8a2a3e"/>
        <stop offset="1" stop-color="#5a5f7c"/>
      </linearGradient>
      <linearGradient id="panelBlue" x1="0" y1="0" x2="0" y2="1">
        <stop offset="0" stop-color="#2a5cb6"/>
        <stop offset="1" stop-color="#233a8c"/>
      </linearGradient>
      <radialGradient id="productTone" cx="0.5" cy="0.5" r="0.6">
        <stop offset="0" stop-color="#f2f2f2"/>
        <stop offset="1" stop-color="#d9dade"/>
      </radialGradient>
    </defs>
    <g role="img" aria-label="Photo: red fire service valve assembly being measured with a tape measure">
      <path d="M0 0H600V330C540 420 400 470 250 470C140 470 60 440 0 405Z" fill="url(#heroTone)"/>
    </g>
    <path d="M140 462C210 470 280 466 335 450" stroke="var(--red)" stroke-width="5" fill="none" stroke-linecap="round"/>
    <circle cx="90" cy="40" r="112" fill="var(--white)"/>
    <path d="M600 395C560 440 470 470 405 472C370 530 372 640 385 848H600Z" fill="url(#panelBlue)"/>
    <path d="M0 770C110 720 250 730 320 800L350 848H0Z" fill="var(--red)"/>
    <g role="img" aria-label="Product photo: pressure test gauge kit">
      <circle cx="360" cy="455" r="52" fill="none" stroke="#c7c9d3" stroke-dasharray="2 3"/>
      <circle cx="360" cy="455" r="45" fill="var(--white)"/>
      <circle cx="360" cy="455" r="38" fill="url(#productTone)"/>
    </g>
    <g role="img" aria-label="Product photo: bronze gate valve">
      <circle cx="448" cy="398" r="63" fill="none" stroke="#c7c9d3" stroke-dasharray="2 3"/>
      <circle cx="448" cy="398" r="55" fill="var(--white)"/>
      <circle cx="448" cy="398" r="47" fill="url(#productTone)"/>
    </g>
    <g role="img" aria-label="Product photo: backflow preventer assembly">
      <circle cx="548" cy="318" r="78" fill="none" stroke="#c7c9d3" stroke-dasharray="2 3"/>
      <circle cx="548" cy="318" r="69" fill="var(--white)"/>
      <circle cx="548" cy="318" r="60" fill="url(#productTone)"/>
    </g>
  </svg>

  <div class="brand-mark"><span class="brand-mark__dot"></span><span class="brand-mark__name">Valvorim Supply Co.</span></div>

  <section class="hero-text">
    <span class="hero-text__pill">THE NATION'S LEADING SOURCE FOR:</span>
    <p class="hero-text__line hero-text__oem">GENUINE OEM PARTS</p>
    <p class="hero-text__line hero-text__repair">REPAIR</p>
    <p class="hero-text__line hero-text__info">INFORMATION</p>
    <p class="hero-text__line hero-text__tech">TECHNICAL ASSISTANCE</p>
  </section>

  <section class="repair-matrix">
    <h2 class="repair-matrix__title">REPAIR</h2>
    <h3 class="repair-matrix__sub">MATRIX</h3>
    <p class="repair-matrix__hint">SELECT YOUR ASSEMBLY SIZE AND MODEL TO SEE PARTS.</p>
    <div class="brand-grid">
      <span class="brand-grid__tile">KESTREL</span>
      <span class="brand-grid__tile">BRANDT</span>
      <span class="brand-grid__tile">OLSEN</span>
      <span class="brand-grid__tile">TARVO</span>
      <span class="brand-grid__tile">PENNICK</span>
      <span class="brand-grid__tile">RUSKIN</span>
      <span class="brand-grid__tile">QUELLO</span>
      <span class="brand-grid__tile">DORRAN</span>
      <span class="brand-grid__tile">NEVIS</span>
      <span class="brand-grid__tile">GRAYLE</span>
      <span class="brand-grid__tile">LORNE</span>
      <span class="brand-grid__tile">VESPER</span>
    </div>
  </section>

  <ul class="advantages">
    <li class="advantages__item"><span class="advantages__icon"><svg width="12" height="12" viewBox="0 0 12 12"><path d="M2 6.5l2.5 2.5L10 3" stroke="var(--red)" stroke-width="2" fill="none"/></svg></span>Genuine OEM<br>Parts</li>
    <li class="advantages__item"><span class="advantages__icon"><svg width="12" height="12" viewBox="0 0 12 12"><path d="M2 6.5l2.5 2.5L10 3" stroke="var(--red)" stroke-width="2" fill="none"/></svg></span>Technical assistance from<br>repair experts</li>
    <li class="advantages__item"><span class="advantages__icon"><svg width="12" height="12" viewBox="0 0 12 12"><path d="M2 6.5l2.5 2.5L10 3" stroke="var(--red)" stroke-width="2" fill="none"/></svg></span>Repair<br>information</li>
    <li class="advantages__item"><span class="advantages__icon"><svg width="12" height="12" viewBox="0 0 12 12"><path d="M2 6.5l2.5 2.5L10 3" stroke="var(--red)" stroke-width="2" fill="none"/></svg></span>1-2 day delivery across the<br>United States</li>
    <li class="advantages__item"><span class="advantages__icon"><svg width="12" height="12" viewBox="0 0 12 12"><path d="M2 6.5l2.5 2.5L10 3" stroke="var(--red)" stroke-width="2" fill="none"/></svg></span>Friendly &amp; knowledgeable<br>customer service</li>
    <li class="advantages__item"><span class="advantages__icon"><svg width="12" height="12" viewBox="0 0 12 12"><path d="M2 6.5l2.5 2.5L10 3" stroke="var(--red)" stroke-width="2" fill="none"/></svg></span>Largest parts inventory in<br>the nation</li>
    <li class="advantages__item"><span class="advantages__icon"><svg width="12" height="12" viewBox="0 0 12 12"><path d="M2 6.5l2.5 2.5L10 3" stroke="var(--red)" stroke-width="2" fill="none"/></svg></span>Testing equipment<br>available</li>
    <li class="advantages__item"><span class="advantages__icon"><svg width="12" height="12" viewBox="0 0 12 12"><path d="M2 6.5l2.5 2.5L10 3" stroke="var(--red)" stroke-width="2" fill="none"/></svg></span>Full-service gauge<br>calibration &amp; repair</li>
  </ul>

  <section class="contact">
    <div class="contact__row">
      <span class="contact__icon"><svg width="12" height="12" viewBox="0 0 24 24"><path d="M6.6 10.8a15.1 15.1 0 006.6 6.6l2.2-2.2a1 1 0 011-.25 11.4 11.4 0 003.6.57 1 1 0 011 1V20a1 1 0 01-1 1A17 17 0 013 4a1 1 0 011-1h3.5a1 1 0 011 1c0 1.250.2 2.450.57 3.57a1 1 0 01-.25 1z" fill="#fff"/></svg></span>
      <span><span class="contact__label">PHONE:</span><span class="contact__value">(800) 312-4470</span></span>
    </div>
    <div class="contact__row">
      <span class="contact__icon"><svg width="12" height="12" viewBox="0 0 24 24"><circle cx="12" cy="12" r="9" stroke="#fff" stroke-width="2" fill="none"/><path d="M3 12h18M12 3c3 3 3 15 0 18M12 3c-3 3-3 15 0 18" stroke="#fff" stroke-width="1.6" fill="none"/></svg></span>
      <span><span class="contact__label">WEBSITE:</span><span class="contact__value">www.valvorimsupply.com</span></span>
    </div>
  </section>
</main>
</body>
</html>
```